Event Graphics Needed for Kid's Conference

I am in need of graphics for our event, Prairie Youth Gathering also known as TotFest21. It is a conference event for elementary students - 1st - 5th grade. The theme for the event is "The Heart Rises" and the graphics/imagery should be Moon Quest themed as that is our theme for the event. I am not aware of the copyright issues with moon quest - style design so please make yourself aware of those legal concerns.
I need title graphics as well as an 11x17 event poster. Title graphics should include sizes for social, 3x4 postcard, & 16x9 for projected screens. Graphic should include the following logo: the PW BrightPath logo (this is our organization). Additionally, the poster should include the following information:
Millbrook Grace Chapel
Millbrook, SD
February 12-13, 2021
Guest Speakers: Dorian & Lee Whitfield (see picture)
(may add a website here but will confirm before final approval)
Target Market(s)
Children Kindergarten through 5th grade
Look and feel
Each slider illustrates characteristics of the customer's brand and the style your logo design should communicate.

```html
<!DOCTYPE html>
<html lang="en">
<head>
<meta charset="utf-8">
<title>TotFest21 – The Heart Rises</title>
<link href="https://fonts.googleapis.com/css2?family=Montserrat:wght@400;500;700;900&family=Oswald:wght@700&display=swap" rel="stylesheet">
<style>
  :root {
    --space-deep: #03050c;
    --space-mid: #0a1a3a;
    --space-glow: #1d4f8f;
    --title-navy: #16213a;
    --glow-red: #e0141c;
    --beam-blue: #3aa8ff;
    --logo-cyan: #2ec0f0;
    --text-white: #ffffff;
    --footer-band: #0f2236;
    --divider: #2bb8e0;
  }
  * { margin: 0; padding: 0; box-sizing: border-box; }
  html, body { width: 878px; height: 1200px; overflow: hidden; background: var(--space-deep); }
  .poster {
    position: relative; width: 878px; height: 1200px; overflow: hidden;
    font-family: "Montserrat", sans-serif; color: var(--text-white);
    background:
      radial-gradient(ellipse 60% 35% at 55% 38%, rgba(40,110,200,0.55), transparent 70%),
      radial-gradient(ellipse 50% 25% at 30% 20%, rgba(30,80,150,0.45), transparent 70%),
      linear-gradient(180deg, #050914 0%, var(--space-mid) 35%, #081326 60%, var(--space-deep) 100%);
  }
  .space-backdrop { position: absolute; inset: 0; }
  .org-mark {
    position: absolute; top: 92px; left: 0; width: 100%;
    display: flex; justify-content: center; align-items: center; gap: 12px;
  }
  .org-mark .dot { width: 22px; height: 22px; border-radius: 50%; background: var(--logo-cyan); }
  .org-mark .name { font-weight: 900; font-size: 40px; color: var(--logo-cyan); letter-spacing: 1px; }
  .presents {
    position: absolute; top: 190px; width: 100%; text-align: center;
    font-size: 15px; font-weight: 500; letter-spacing: 6px;
  }
  .light-beams { position: absolute; left: 0; top: 560px; width: 878px; height: 260px; }
  .speaker-photo {
    position: absolute; left: 150px; top: 272px; width: 620px; height: 420px;
    border-radius: 180px 180px 20px 20px;
    background: radial-gradient(ellipse at 50% 40%, #b08a78 0%, #6c6f86 45%, #2a3350 80%, rgba(20,30,60,0) 100%);
  }
  .title-main {
    position: absolute; top: 636px; width: 100%; text-align: center;
    font-weight: 900; font-size: 158px; line-height: 1; letter-spacing: -4px;
    color: var(--title-navy);
    text-shadow: 0 0 6px var(--glow-red), 0 0 18px rgba(224,20,28,0.7);
  }
  .tagline {
    position: absolute; top: 796px; width: 100%; text-align: center;
    font-weight: 700; font-size: 21px; letter-spacing: 7px;
    text-shadow: 0 0 8px rgba(0,0,0,0.8);
  }
  .title-sub {
    position: absolute; top: 826px; width: 100%; text-align: center;
    font-weight: 900; font-size: 78px; line-height: 1; letter-spacing: -1px;
    color: var(--title-navy);
    text-shadow: 0 0 6px var(--glow-red), 0 0 18px rgba(224,20,28,0.7);
  }
  .audience {
    position: absolute; top: 916px; width: 100%; text-align: center;
    font-size: 20px; font-weight: 400;
  }
  .grade-box {
    position: absolute; left: 348px; top: 960px; width: 182px; height: 44px;
    border: 1.5px solid var(--text-white); border-radius: 5px;
    text-align: center; font-size: 25px; line-height: 42px; font-weight: 400;
  }
  .grade-box .label {
    position: absolute; top: -14px; left: 50%; transform: translateX(-50%);
    background: #040812; padding: 0 6px; font-size: 19px; font-weight: 700; line-height: 22px;
  }
  .divider {
    position: absolute; left: 438px; top: 1020px; width: 2px; height: 112px;
    background: linear-gradient(180deg, transparent, var(--divider), transparent);
  }
  .speakers { position: absolute; left: 160px; top: 1040px; width: 240px; text-align: center; }
  .speakers .label { font-size: 15px; font-weight: 400; margin-bottom: 12px; }
  .speakers .person { font-size: 23px; font-weight: 700; line-height: 33px; white-space: nowrap; }
  .event-date { position: absolute; left: 495px; top: 1040px; width: 140px; }
  .event-date .month { font-size: 21px; font-weight: 700; letter-spacing: 1px; }
  .event-date .days {
    display: flex; align-items: stretch; margin-top: 2px;
  }
  .event-date .range {
    background: var(--text-white); color: #000; font-family: "Oswald", sans-serif;
    font-weight: 700; font-size: 48px; line-height: 54px; padding: 0 4px; letter-spacing: -1px;
  }
  .event-date .year {
    writing-mode: vertical-rl; transform: rotate(180deg);
    font-weight: 900; font-size: 13px; letter-spacing: 1px; padding-left: 2px;
  }
  .info-band {
    position: absolute; left: 0; top: 1157px; width: 100%; height: 31px;
    background: var(--footer-band);
    display: flex; align-items: center; justify-content: space-between;
    padding: 0 22px; font-size: 15px; font-weight: 400; letter-spacing: 0.3px;
  }
  .info-band .venue, .info-band .web { display: flex; align-items: center; gap: 5px; }
  .info-band .city { margin-left: 16px; }
</style>
</head>
<body>
<main class="poster">
  <svg class="space-backdrop" width="878" height="1200" role="img" aria-label="Starfield nebula background">
    <defs>
      <radialGradient id="nebula" cx="50%" cy="50%" r="50%">
        <stop offset="0%" stop-color="#2a6bbf" stop-opacity="0.35"/>
        <stop offset="100%" stop-color="#2a6bbf" stop-opacity="0"/>
      </radialGradient>
    </defs>
    <ellipse cx="250" cy="330" rx="240" ry="160" fill="url(#nebula)"/>
    <ellipse cx="640" cy="200" rx="220" ry="140" fill="url(#nebula)"/>
  </svg>

  <div class="org-mark"><span class="dot"></span><span class="name">PW BrightPath</span></div>
  <div class="presents">PRESENTS</div>

  <svg class="light-beams" viewBox="0 0 878 260" preserveAspectRatio="none">
    <path d="M0 110 Q300 170 600 60 T878 20" stroke="#e0141c" stroke-width="6" fill="none" opacity="0.85"/>
    <path d="M0 110 Q300 170 600 60 T878 20" stroke="#ffd0d0" stroke-width="1.5" fill="none"/>
    <path d="M0 220 Q350 180 620 150 T878 100" stroke="#3aa8ff" stroke-width="6" fill="none" opacity="0.85"/>
    <path d="M0 220 Q350 180 620 150 T878 100" stroke="#e6f4ff" stroke-width="1.5" fill="none"/>
  </svg>

  <div class="speaker-photo" role="img" aria-label="Photo of guest speakers Dorian and Lee Whitfield smiling together"></div>

  <h1 class="title-main">TOT</h1>
  <p class="tagline">THE HEART RISES</p>
  <p class="title-sub">FEST 21</p>
  <p class="audience">A CONFERENCE EVENT FOR ELEMENTARY STUDENTS</p>
  <div class="grade-box"><span class="label">GRADE</span>1ST - 5TH</div>

  <div class="divider"></div>

  <section class="speakers">
    <p class="label">GUEST SPEAKER</p>
    <p class="person">LEE WHITFIELD</p>
    <p class="person">DORIAN WHITFIELD</p>
  </section>

  <section class="event-date">
    <p class="month">FEBRUARY</p>
    <div class="days"><span class="range">12-13</span><span class="year">2021</span></div>
  </section>

  <footer class="info-band">
    <span class="venue">
      <svg width="10" height="14" viewBox="0 0 10 14"><path d="M5 0a5 5 0 0 0-5 5c0 4 5 9 5 9s5-5 5-9a5 5 0 0 0-5-5zm0 7a2 2 0 1 1 0-4 2 2 0 0 1 0 4z" fill="#fff"/></svg>
      MILLBROOK GRACE CHAPEL<span class="city">MILLBROOK, SD</span>
    </span>
    <span class="web">
      <svg width="12" height="12" viewBox="0 0 12 12" fill="none" stroke="#fff" stroke-width="1"><circle cx="6" cy="6" r="5"/><ellipse cx="6" cy="6" rx="2.2" ry="5"/><line x1="1" y1="6" x2="11" y2="6"/></svg>
      PWYOUTHGATHERING.COM
    </span>
  </footer>
</main>
</body>
</html>
```